KV HOLDWELL GROUP LETTERHEAD

I need letterhead for "KV Holdwell group LLC" ...

logo attached to project...

Company Info:
845 North Marlow Avenue, Suite 7B
Chicago, Illinois 60611
ofc 312-555-0184
facsimile 312-555-0172
www.kvholdwellgroup.example
info@kvholdwellgroup.example

I have multiple projects listed.. see below:

Business cards for ashford lane equity llc
letterhead
envelopes

Business cards for KV Holdwell LLC
letterhead
envelopes

```html
<!DOCTYPE html>
<html lang="en">
<head>
<meta charset="utf-8">
<title>KV Holdwell Group LLC — Stationery</title>
<link href="https://fonts.googleapis.com/css2?family=Tinos:wght@400;700&family=Open+Sans:wght@400;600&display=swap" rel="stylesheet">
<style>
  :root {
    --bg: #e4e4e4;
    --paper: #ffffff;
    --blue-deep: #0d3f8f;
    --blue-mid: #1c5fb8;
    --blue-light: #3b7fd4;
    --ink: #1d1d1d;
    --ink-blue: #1a4f9c;
    --rule: #9fb4d6;
  }
  * { box-sizing: border-box; margin: 0; padding: 0; }
  html, body { width: 1200px; height: 884px; overflow: hidden; background: var(--bg); }
  .canvas { position: relative; width: 1200px; height: 884px; }

  .brand-name {
    font-family: "Tinos", serif;
    font-weight: 400;
    color: var(--blue-deep);
    letter-spacing: 0.04em;
    white-space: nowrap;
  }
  .brand-dot {
    display: inline-block;
    border-radius: 50%;
    background: var(--blue-deep);
    vertical-align: middle;
  }

  /* Letterhead */
  .letterhead {
    position: absolute; left: 110px; top: 70px;
    width: 572px; height: 740px;
    background: var(--paper);
    box-shadow: 0 2px 10px rgba(0,0,0,0.12);
  }
  .letterhead-header { position: absolute; left: 0; top: 0; width: 100%; height: 118px; }
  .letterhead-header svg { display: block; }
  .letterhead-brand {
    position: absolute; left: 0; right: 0; top: 40px;
    display: flex; flex-direction: column; align-items: center; gap: 6px;
  }
  .letterhead-brand .brand-dot { width: 26px; height: 26px; }
  .letterhead-brand .brand-name { font-size: 13px; }

  .letter-body {
    position: absolute; left: 62px; right: 62px; top: 150px;
    font-family: "Tinos", serif; color: var(--ink);
    font-size: 11.2px; line-height: 1.32; text-align: justify;
  }
  .letter-greeting { color: var(--ink-blue); font-weight: 700; font-size: 12px; margin-bottom: 10px; }
  .letter-body p { margin-bottom: 11px; }

  .letterhead-footer {
    position: absolute; left: 56px; right: 24px; bottom: 36px;
    display: flex; align-items: flex-start;
    font-family: "Open Sans", sans-serif; font-size: 8.8px; line-height: 1.45;
    color: var(--ink-blue); font-weight: 600;
  }
  .footer-col { padding: 0 14px; white-space: nowrap; }
  .footer-col:first-child { padding-left: 0; }
  .footer-col + .footer-col { border-left: 1px solid var(--rule); }

  /* Business cards */
  .card {
    position: absolute; width: 340px; height: 196px;
    background: var(--paper); overflow: hidden;
    box-shadow: 0 2px 8px rgba(0,0,0,0.14);
  }
  .card svg { position: absolute; left: 0; top: 0; }
  .card-front { left: 770px; top: 170px; }
  .card-back { left: 770px; top: 430px; }

  .card-front .card-brand {
    position: absolute; left: 0; right: 0; top: 104px;
    display: flex; align-items: center; justify-content: center; gap: 8px;
  }
  .card-front .brand-dot { width: 20px; height: 20px; }
  .card-front .brand-name { font-size: 15px; }

  .card-back .card-brand {
    position: absolute; left: 0; right: 0; top: 20px;
    display: flex; align-items: center; justify-content: center; gap: 6px;
  }
  .card-back .brand-dot { width: 14px; height: 14px; background: var(--paper); }
  .card-back .brand-name { font-size: 10px; color: var(--paper); }
  .card-contact {
    position: absolute; left: 24px; right: 20px; bottom: 18px;
    display: flex; gap: 18px;
    font-family: "Open Sans", sans-serif; font-size: 7px; line-height: 1.5;
    color: var(--paper);
  }
  .card-contact .contact-col { white-space: nowrap; }
  .card-contact .contact-col + .contact-col { border-left: 1px solid rgba(255,255,255,0.6); padding-left: 14px; }
  .card-contact strong { font-weight: 600; }
</style>
</head>
<body>
<main class="canvas">

  <section class="letterhead">
    <div class="letterhead-header">
      <svg width="572" height="118" viewBox="0 0 572 118" aria-hidden="true">
        <defs>
          <linearGradient id="bandBlue" x1="0" y1="0" x2="1" y2="1">
            <stop offset="0" stop-color="#0d3f8f"/>
            <stop offset="0.5" stop-color="#1c5fb8"/>
            <stop offset="1" stop-color="#0d3f8f"/>
          </linearGradient>
        </defs>
        <rect x="0" y="0" width="572" height="62" fill="url(#bandBlue)"/>
        <polygon points="0,0 180,0 90,62 0,62" fill="#ffffff" opacity="0.06"/>
        <polygon points="400,0 572,0 572,62 480,62" fill="#ffffff" opacity="0.07"/>
        <ellipse cx="286" cy="50" rx="78" ry="56" fill="#ffffff"/>
      </svg>
      <div class="letterhead-brand">
        <span class="brand-dot"></span>
        <span class="brand-name">KV Holdwell group LLC</span>
      </div>
    </div>

    <div class="letter-body">
      <div class="letter-greeting">Lorem ipsum dolor sit amet,</div>
      <p>Lorem ipsum dolor sit amet, consectetur adipiscing elit. Donec orci purus, luctus vitae dignissim eu, iaculis sed purus. Vivamus faucibus, ipsum nec aliquet viverra, leo mauris condimentum ligula, sit amet sagittis enim ligula quis arcu. Nam egestas tortor id nisi porttitor mattis. In tortor ante, ultricies in suscipit a, tempus non massa. Vivamus et auctor mi. Fusce vel massa nulla. Phasellus nec eros mauris, et scelerisque orci. Donec malesuada orci vitae nulla accumsan porta a id massa. Quisque accumsan iaculis magna sit amet fringilla. Maecenas consequat, magna eget tincidunt semper, odio nibh rutrum mi, id feugiat ante nisi eu risus. Vestibulum nunc orci, rhoncus a placerat in, ultricies in mi. Cras mattis varius eros, vel fringilla nisi suscipit eget.</p>
      <p>Quisque scelerisque sagittis nulla at porttitor. Mauris a justo et tellus interdum tristique. Sed id augue vitae urna euismod commodo aliquet a quam. Pellentesque arcu velit, cursus et malesuada ut, consequat et diam. Nullam erat sem, rhoncus id ullamcorper vitae, rhoncus et arcu. In ultricies ultricies nulla, ut rutrum nisi iaculis at. Donec eu magna a metus ornare faucibus. Fusce aliquet faucibus ultricies. Morbi semper, est id tincidunt gravida, sem arcu adipiscing lacus, ac bibendum nulla leo eu purus. Quisque nec diam sed risus consectetur a ecumsan quis quis nibh. Vestibulum id purus lorem.</p>
      <p>Vivamus vehicula accumsan lacinia. Aliquam erat volutpat. Pellentesque consequat venenatis velit non gravida. Etiam et sem et nulla congue aliquam sed eget augue. Nulla facilisi. Pellentesque habitant morbi tristique senectus et netus et malesuada fames ac turpis egestas. Nulla a elit at sem iaculis congue. Nullam mollis tristique lobortis.</p>
    </div>

    <footer class="letterhead-footer">
      <div class="footer-col">845 North Marlow Avenue, Suite 7B<br>Chicago, Illinois 60611</div>
      <div class="footer-col">ofc 312-555-0184<br>facsimile 312-555-0172</div>
      <div class="footer-col">www.kvholdwellgroup.example<br>info@kvholdwellgroup.example</div>
    </footer>
  </section>

  <section class="card card-front">
    <svg width="340" height="196" viewBox="0 0 340 196" aria-hidden="true">
      <defs>
        <linearGradient id="cardBlue" x1="0" y1="0" x2="1" y2="1">
          <stop offset="0" stop-color="#0d3f8f"/>
          <stop offset="0.6" stop-color="#1c5fb8"/>
          <stop offset="1" stop-color="#0d3f8f"/>
        </linearGradient>
      </defs>
      <rect x="0" y="0" width="340" height="196" fill="url(#cardBlue)"/>
      <path d="M0,92 C110,30 240,20 340,40 L340,196 L0,196 Z" fill="#ffffff"/>
    </svg>
    <div class="card-brand">
      <span class="brand-dot"></span>
      <span class="brand-name">KV HOLDWELL GROUP LLC</span>
    </div>
  </section>

  <section class="card card-back">
    <svg width="340" height="196" viewBox="0 0 340 196" aria-hidden="true">
      <rect x="0" y="0" width="340" height="196" fill="url(#cardBlue)"/>
      <path d="M0,58 C120,90 230,90 340,62 L340,100 C230,124 110,122 0,96 Z" fill="#ffffff"/>
    </svg>
    <div class="card-brand">
      <span class="brand-dot"></span>
      <span class="brand-name">KV Holdwell LLC</span>
    </div>
    <div class="card-contact">
      <div class="contact-col">
        <strong>Daniel R. Moss</strong><br>Managing Partner<br>ofc 312-555-0184<br>info@kvholdwellgroup.example
      </div>
      <div class="contact-col">
        845 North Marlow Avenue, Suite 7B<br>Chicago, Illinois 60611<br>fax 312-555-0172<br>www.kvholdwellgroup.example
      </div>
    </div>
  </section>

</main>
</body>
</html>
```